Need a book cover design for a Lumora Book

Book has a long title and sub title so lots of words to fit on the cover.

I can be flexible a bit with the sub title due to the length of it but ideally i can get a design that takes everything.

Here is the title:

Tidal Geology: The Roots of Erosion, Sedimentation, and Canyon Forming

Sub Title/Heading
An Easy Primer on Coastal Cliffs, Dune Drift, River Beds, and Delta Mapping Methods

```html
<!DOCTYPE html>
<html lang="en">
<head>
<meta charset="UTF-8">
<title>Tidal Geology – Book Cover</title>
<link href="https://fonts.googleapis.com/css2?family=Barlow:wght@500;600&family=Barlow+Semi+Condensed:wght@500;600&display=swap" rel="stylesheet">
<style>
  :root {
    --stage: #3b3b3b;
    --cover-deep: #01060f;
    --cover-mid: #041229;
    --band: #03295a;
    --band-edge: #0b3c78;
    --ice: #b8dbfd;
    --ice-soft: #9cc6f2;
    --title-light: #a9d2fb;
    --title-dark: #1c4476;
    --glow-core: #1fa6ec;
    --glow-mid: #1560b8;
    --glow-outer: #0a2d66;
  }
  * { margin: 0; padding: 0; box-sizing: border-box; }
  html, body {
    width: 1200px; height: 1200px; overflow: hidden;
    background: var(--stage);
  }
  .cover {
    position: absolute; left: 222px; top: 32px;
    width: 757px; height: 1136px; overflow: hidden;
    background: radial-gradient(ellipse at 50% 58%, var(--cover-mid) 0%, var(--cover-deep) 70%);
    font-family: "Barlow Semi Condensed", "Barlow", sans-serif;
    color: var(--ice);
  }
  .band {
    position: absolute; left: 0; width: 100%; z-index: 3;
    background: var(--band);
  }
  .band--top {
    top: 0; height: 28px;
    border-bottom: 1px solid var(--band-edge);
    background: linear-gradient(115deg, var(--band) 0%, var(--band) 88%, var(--ice) 94%, var(--band) 100%);
  }
  .band--bottom {
    bottom: 0; height: 70px;
    border-top: 1px solid var(--band-edge);
    background: linear-gradient(115deg, var(--ice) 0%, var(--band) 16%, var(--band) 100%);
    display: flex; align-items: center; justify-content: center;
  }
  .author {
    font-weight: 600; font-size: 30px; letter-spacing: 0.5px;
    color: var(--ice);
  }
  .illustration {
    position: absolute; left: 59px; top: 322px;
    width: 680px; height: 680px; border-radius: 50%; z-index: 1;
    background: radial-gradient(circle at 50% 50%, var(--glow-core) 0%, var(--glow-mid) 26%, var(--glow-outer) 50%, rgba(10,45,102,0.35) 62%, rgba(4,18,41,0) 74%);
  }
  .title {
    position: absolute; left: 0; top: 0; width: 757px; height: 330px; z-index: 2;
  }
  .title text {
    font-family: "Barlow", sans-serif; font-weight: 500;
  }
  .series-line {
    position: absolute; left: 0; width: 100%; text-align: center; z-index: 2;
    font-weight: 600; font-size: 27px; line-height: 31px;
    color: var(--ice); letter-spacing: 0.2px; white-space: nowrap;
  }
  .series-line--one { top: 330px; }
  .series-line--two {
    top: 362px;
    display: flex; align-items: center; justify-content: center; gap: 16px;
  }
  .rule { width: 160px; height: 2px; background: var(--ice); }
  .primer {
    position: absolute; left: 0; top: 942px; width: 100%; z-index: 2;
    text-align: center; font-weight: 600; font-size: 29px; line-height: 33px;
    color: var(--ice); white-space: nowrap;
  }
</style>
</head>
<body>
  <main class="cover">
    <div class="band band--top"></div>

    <div class="illustration" role="img" aria-label="Glowing blue sphere illustration with orbiting rings around a central cluster"></div>

    <svg class="title" viewBox="0 0 757 330" aria-label="Tidal Geology">
      <defs>
        <linearGradient id="titleFill" x1="0" y1="0" x2="1" y2="0">
          <stop offset="0" stop-color="var(--title-dark)"/>
          <stop offset="0.45" stop-color="var(--title-light)"/>
          <stop offset="0.7" stop-color="var(--ice-soft)"/>
          <stop offset="1" stop-color="var(--title-dark)"/>
        </linearGradient>
      </defs>
      <text x="378" y="173" text-anchor="middle" font-size="150" letter-spacing="8"
            fill="url(#titleFill)" stroke="#7fa6cf" stroke-width="1.2">TIDAL</text>
      <text x="378" y="306" text-anchor="middle" font-size="146" textLength="600" lengthAdjust="spacingAndGlyphs"
            fill="url(#titleFill)" stroke="#7fa6cf" stroke-width="1.2">GEOLOGY</text>
    </svg>

    <p class="series-line series-line--one">THE ROOTS OF EROSION, SEDIMENTATION,</p>
    <p class="series-line series-line--two"><span class="rule"></span>AND CANYON FORMING<span class="rule"></span></p>

    <p class="primer">AN EASY PRIMER ON COASTAL CLIFFS,<br>DUNE DRIFT, RIVER BEDS, AND DELTA<br>MAPPING METHODS</p>

    <div class="band band--bottom"><span class="author">AUTHOR NAME</span></div>
  </main>
</body>
</html>
```